Security Warning Sign

We have an existing sign that needs an update. I have attached a picture of the current square sign. We need to maintain the same wording. It needs to be professional and appropriate to attach to our customers fence. Also attached is a copy of our building sign which may lend some inspiration and hopefully the ai format will assist. The final sign will be 600mm x 600mmOur website is www.halvorngate.com.au

```html
<!DOCTYPE html>
<html lang="en">
<head>
<meta charset="utf-8">
<title>Warning – Electronic Surveillance Sign</title>
<link href="https://fonts.googleapis.com/css2?family=Anton&family=Questrial&family=Open+Sans:wght@800&display=swap" rel="stylesheet">
<style>
  :root {
    --orange: #f28322;
    --white: #ffffff;
    --ink: #0d0d0d;
    --charcoal: #242526;
    --charcoal-deep: #1b1c1d;
    --yellow: #fcc917;
    --yellow-edge: #ffe000;
  }
  html, body {
    margin: 0;
    padding: 0;
    width: 1200px;
    height: 1200px;
    overflow: hidden;
    background: var(--white);
  }
  .sign {
    display: block;
    width: 1200px;
    height: 1200px;
  }
  .sign__frame { fill: var(--white); stroke: var(--orange); stroke-width: 14; }
  .headline {
    font-family: "Anton", "Oswald", sans-serif;
    font-size: 182px;
    fill: var(--ink);
  }
  .notice {
    font-family: "Questrial", "Helvetica Neue", sans-serif;
    font-size: 88px;
    fill: var(--ink);
  }
  .brand-band { fill: url(#bandShade); }
  .brand-name {
    font-family: "Open Sans", "Arial", sans-serif;
    font-weight: 800;
    font-size: 72px;
    fill: var(--white);
  }
  .brand-mark { fill: var(--orange); }
  .contact {
    font-family: "Open Sans", "Arial", sans-serif;
    font-weight: 800;
    fill: var(--white);
  }
  .contact--web { font-size: 37px; }
  .contact--phone { font-size: 52px; }
  .phone-panel { fill: var(--orange); }
  .phone-icon { fill: var(--charcoal); }
</style>
</head>
<body>
<svg class="sign" viewBox="0 0 1200 1200" xmlns="http://www.w3.org/2000/svg" role="img" aria-label="Warning: electronic surveillance and recording installed in this area">
  <defs>
    <linearGradient id="bandShade" x1="0" y1="0" x2="1" y2="1">
      <stop offset="0" stop-color="#2a2b2c"/>
      <stop offset="0.5" stop-color="#1e1f20"/>
      <stop offset="1" stop-color="#262728"/>
    </linearGradient>
  </defs>

  <!-- Notice panel -->
  <rect class="sign__frame" x="22" y="23" width="1156" height="774"/>

  <g class="hazard-icon">
    <path d="M296 72 L200 243 L393 240 Z" fill="var(--yellow-edge)" stroke="var(--yellow-edge)" stroke-width="30" stroke-linejoin="round"/>
    <path d="M296 72 L200 243 L393 240 Z" fill="var(--ink)" stroke="var(--ink)" stroke-width="20" stroke-linejoin="round"/>
    <path d="M296 92 L215 236 L378 234 Z" fill="var(--yellow)" stroke="var(--yellow)" stroke-width="8" stroke-linejoin="round"/>
    <path d="M282 113 Q282 110 286 110 L305 110 Q309 110 309 113 L303 182 L288 182 Z" fill="var(--ink)"/>
    <circle cx="296" cy="207" r="14" fill="var(--ink)"/>
  </g>

  <text class="headline" x="404" y="232" textLength="591" lengthAdjust="spacingAndGlyphs">WARNING</text>

  <g class="notice-lines" text-anchor="middle">
    <text class="notice" x="586" y="344" textLength="529" lengthAdjust="spacingAndGlyphs">ELECTRONIC</text>
    <text class="notice" x="587" y="437" textLength="746" lengthAdjust="spacingAndGlyphs">SURVEILLANCE &amp;</text>
    <text class="notice" x="586" y="533" textLength="505" lengthAdjust="spacingAndGlyphs">RECORDING</text>
    <text class="notice" x="601" y="628" textLength="465" lengthAdjust="spacingAndGlyphs">INSTALLED</text>
    <text class="notice" x="601" y="724" textLength="574" lengthAdjust="spacingAndGlyphs">IN THIS AREA</text>
  </g>

  <!-- Brand band -->
  <rect class="brand-band" x="0" y="820" width="1200" height="380"/>

  <circle class="brand-mark" cx="356" cy="985" r="100"/>
  <g class="brand-lockup">
    <text class="brand-name" x="520" y="941" textLength="461" lengthAdjust="spacingAndGlyphs">HALVORNGATE</text>
    <text class="brand-name" x="520" y="1009" textLength="351" lengthAdjust="spacingAndGlyphs">SECURITY</text>
    <text class="brand-name" x="520" y="1079" textLength="336" lengthAdjust="spacingAndGlyphs">SERVICES</text>
  </g>

  <text class="contact contact--web" x="40" y="1173" textLength="655" lengthAdjust="spacingAndGlyphs">WWW.HALVORNGATE.COM.AU</text>

  <polygon class="phone-panel" points="718,1200 771,1113 784,1113 731,1200"/>
  <polygon class="phone-panel" points="744,1200 797,1113 1200,1113 1200,1200"/>

  <g class="phone-icon" transform="translate(790 1136) scale(1.9)">
    <path d="M6.6 10.8c1.4 2.8 3.8 5.1 6.6 6.6l2.2-2.2c.3-.3.7-.4 1-.2 1.1.4 2.3.6 3.6.6.6 0 1 .4 1 1V20c0 .6-.4 1-1 1C10.6 21 3 13.4 3 4c0-.6.4-1 1-1h3.5c.6 0 1 .4 1 1 0 1.3.2 2.5.6 3.6.1.3 0 .7-.2 1z"/>
  </g>
  <text class="contact contact--phone" x="849" y="1178" textLength="308" lengthAdjust="spacingAndGlyphs">1300 555 014</text>
</svg>
</body>
</html>
```